Real Estate Flyer (Brenton Property)

We need a color CMYK high resolution, print quality horizontal real estate property flyer designed in the sizes of 10" wide and 6.7425" tall and another one in 11" wide and 8.5" tall.
Ad should be professionally looking to U.S. standards. It should be sleek, modern yet classy.
We uploaded in Briefs logo files, agent photo, 2 photos of the property (Must use both) and a sample of a flyer for Vayle Morrow Luxury Residence. We like how the overlay atop the first photo in the Vayle Morrow flyer with the company logo in the overlay. We'd like to incorporate that with our logo, the background color of the overlay should match that of our logo. DON'T CHANGE LOGO COLORS. Only use two colors in ad (exact logo blue color and white). The text in the overlay must be "FOR SALE - Potential Income Producing Commercial Office Building". Other details that should be prominent underneath are "42 Brenton Dr., Schaumburg, IL 60174 - Asking Price: $650,000".
Add "Residential & Commercial" under our company logo in italic font.
Add in flyer: "Located seconds away from the Kettering Rd. & Palden Rd. Intersection"
Add in flyer:
- Completely vacant
- 10,000 sq. ft. building
- 55 Car Parking
- 1.38 acre lot
- Over 20 offices and 5 bathrooms.
- Lease out individual office spaces for great monthly cash flow
Put agent's photo and following details professionally displayed:
Dev Marlo
Managing Broker
847-555-0148
dev.marlo@qtnhomes-example.com
Add from Briefs fair housing logo and PLX logo near agent's information. Logos should be small but yet visible to understand text.
Add at bottom of the ad with separation near agent details:
Looking to Buy or Sell?
I’m your one-stop, full service licensed real estate broker.
I deal with all types of real estate properties: Homes, Condos, Townhomes, Multi-Unit Apartment Buildings and Commercial Spaces.
Let My Experience Guide You Through Every Step of the Process!
Fine print:
©2018 QTN Homes, Inc. All Rights Reserved.

```html
<!DOCTYPE html>
<html lang="en">
<head>
<meta charset="utf-8">
<title>Brenton Property – Commercial Office Building For Sale</title>
<link href="https://fonts.googleapis.com/css2?family=Montserrat:wght@300;400;500;600&family=Source+Serif+4:ital,opsz,wght@0,8..60,400;0,8..60,600;1,8..60,400&display=swap" rel="stylesheet">
<style>
  :root {
    --brand-blue: #0d3fa6;
    --brand-blue-overlay: rgba(13, 63, 166, 0.93);
    --white: #ffffff;
    --ink: #1d2230;
    --rule: #c9ccd4;
    --page: #f3f3f3;
    --sky: #9fbfe0;
    --facade: #e9dcc4;
    --foliage: #c9742c;
    --asphalt: #4a4c55;
  }
  * { box-sizing: border-box; margin: 0; padding: 0; }
  html, body { width: 1200px; height: 746px; overflow: hidden; }
  body { background: var(--page); font-family: "Montserrat", Arial, sans-serif; }

  .flyer {
    position: absolute; left: 80px; top: 23px;
    width: 1039px; height: 700px;
    background: var(--white); overflow: hidden;
    box-shadow: 0 6px 24px rgba(0,0,0,0.12);
  }

  .property-photo { position: absolute; }
  .property-photo--main {
    left: 0; top: 0; width: 699px; height: 504px;
    background: linear-gradient(180deg, var(--sky) 0%, #d9c6a6 30%, var(--facade) 55%, var(--foliage) 72%, #6d5a45 86%, var(--asphalt) 100%);
  }
  .property-photo--lot {
    left: 699px; top: 483px; width: 340px; height: 217px;
    background: linear-gradient(180deg, #d6cfcf 0%, #e4c9a6 35%, #c98a55 55%, #6a6a72 72%, var(--asphalt) 100%);
  }

  .features {
    position: absolute; left: 699px; top: 0; width: 340px; height: 353px;
    background: var(--white);
  }
  .features__strip { height: 36px; background: var(--brand-blue); }
  .features__location {
    margin: 40px 14px 0 17px; padding-bottom: 14px;
    border-bottom: 1px solid var(--rule);
    font-family: "Source Serif 4", Georgia, serif; font-size: 18.5px; line-height: 1.45;
    color: var(--brand-blue); letter-spacing: -0.4px;
  }
  .features__list { list-style: none; margin: 20px 14px 0 17px; }
  .features__item {
    display: flex; align-items: flex-start; gap: 8px;
    font-size: 13.5px; line-height: 18px; color: var(--ink); margin-bottom: 4px;
  }
  .features__item svg { flex: 0 0 15px; margin-top: 1.5px; }

  .headline-band {
    position: absolute; left: 0; top: 353px; width: 1039px; height: 130px;
    background: var(--brand-blue-overlay); color: var(--white);
  }
  .headline-band__title {
    position: absolute; left: 39px; top: 18px;
    font-family: "Montserrat", Arial, sans-serif; font-weight: 300;
    font-size: 32px; line-height: 36px; text-transform: uppercase; letter-spacing: 0.2px;
  }
  .headline-band__lead {
    font-family: "Source Serif 4", Georgia, serif; font-weight: 600;
    text-transform: none; letter-spacing: -0.3px;
  }
  .headline-band__address {
    position: absolute; left: 39px; top: 99px;
    font-size: 13.5px; font-weight: 500; letter-spacing: 1px; text-transform: uppercase;
  }
  .headline-band__divider {
    position: absolute; left: 769px; top: 15px; width: 1px; height: 105px;
    background: rgba(255,255,255,0.6);
  }
  .brand {
    position: absolute; left: 770px; top: 0; width: 269px; height: 130px;
    display: flex; flex-direction: column; align-items: center; justify-content: center;
  }
  .brand__name {
    display: flex; align-items: center; gap: 8px;
    font-family: "Montserrat", Arial, sans-serif; font-weight: 600; font-size: 26px; color: var(--white);
    letter-spacing: 0.5px;
  }
  .brand__mark { width: 14px; height: 14px; background: var(--white); }
  .brand__tagline {
    margin-top: 10px;
    font-family: "Source Serif 4", Georgia, serif; font-style: italic; font-size: 13.5px; color: var(--white);
  }

  .pitch {
    position: absolute; left: 0; top: 504px; width: 358px; height: 196px;
    background: var(--brand-blue); color: var(--white);
    padding: 30px 36px 0 44px;
  }
  .pitch__title {
    font-family: "Source Serif 4", Georgia, serif; font-weight: 600; font-size: 19px; letter-spacing: -0.3px;
    margin-bottom: 10px;
  }
  .pitch__text { font-size: 10.2px; line-height: 13px; margin-bottom: 13px; }

  .agent-photo {
    position: absolute; left: 358px; top: 504px; width: 107px; height: 196px;
    background: linear-gradient(180deg, #f2f2f2 0%, #dcdcdc 45%, #2a2d35 75%, #15171c 100%);
  }

  .agent {
    position: absolute; left: 465px; top: 504px; width: 234px; height: 196px;
    background: var(--white); padding: 41px 0 0 345px; padding-left: 345px;
  }
  .agent { padding: 41px 0 0 17px; }
  .agent__name { font-family: "Source Serif 4", Georgia, serif; font-weight: 600; font-size: 14.5px; color: var(--ink); }
  .agent__role { font-family: "Source Serif 4", Georgia, serif; font-size: 14.5px; color: var(--ink); margin-top: 1px; }
  .agent__contact {
    display: flex; align-items: center; gap: 6px; margin-top: 6px;
    font-size: 11px; color: var(--brand-blue); letter-spacing: 0.2px;
  }
  .agent__contact--email { margin-top: 4px; text-transform: uppercase; font-size: 10.5px; }
  .agent__badges { display: flex; align-items: center; gap: 12px; margin-top: 18px; }
  .badge { background: #7b7f88; }
  .badge--housing { width: 26px; height: 26px; }
  .badge--listing { width: 72px; height: 30px; background: none; border: 2px solid #7b7f88; }

  .fine-print {
    position: absolute; right: 37px; bottom: 8px;
    font-size: 9.5px; color: var(--white);
  }
</style>
</head>
<body>
  <main class="flyer">
    <div class="property-photo property-photo--main" role="img" aria-label="Photo of the two-storey white office building with dormers and autumn trees"></div>

    <section class="features">
      <div class="features__strip"></div>
      <p class="features__location">Located seconds away from the Kettering Rd. &amp; Palden Rd. Intersection</p>
      <ul class="features__list">
        <li class="features__item"><svg width="15" height="15" viewBox="0 0 15 15"><circle cx="7.5" cy="7.5" r="7.5" fill="#0d3fa6"/><path d="M4 7.7l2.4 2.4L11 5.3" fill="none" stroke="#fff" stroke-width="1.8"/></svg>Completely Vacant</li>
        <li class="features__item"><svg width="15" height="15" viewBox="0 0 15 15"><circle cx="7.5" cy="7.5" r="7.5" fill="#0d3fa6"/><path d="M4 7.7l2.4 2.4L11 5.3" fill="none" stroke="#fff" stroke-width="1.8"/></svg>10,000 sq. ft. Building</li>
        <li class="features__item"><svg width="15" height="15" viewBox="0 0 15 15"><circle cx="7.5" cy="7.5" r="7.5" fill="#0d3fa6"/><path d="M4 7.7l2.4 2.4L11 5.3" fill="none" stroke="#fff" stroke-width="1.8"/></svg>55 Car Parking</li>
        <li class="features__item"><svg width="15" height="15" viewBox="0 0 15 15"><circle cx="7.5" cy="7.5" r="7.5" fill="#0d3fa6"/><path d="M4 7.7l2.4 2.4L11 5.3" fill="none" stroke="#fff" stroke-width="1.8"/></svg>1.38 Acre Lot</li>
        <li class="features__item"><svg width="15" height="15" viewBox="0 0 15 15"><circle cx="7.5" cy="7.5" r="7.5" fill="#0d3fa6"/><path d="M4 7.7l2.4 2.4L11 5.3" fill="none" stroke="#fff" stroke-width="1.8"/></svg>Over 20 offices and 5 bathrooms.</li>
        <li class="features__item"><svg width="15" height="15" viewBox="0 0 15 15"><circle cx="7.5" cy="7.5" r="7.5" fill="#0d3fa6"/><path d="M4 7.7l2.4 2.4L11 5.3" fill="none" stroke="#fff" stroke-width="1.8"/></svg>Lease out individual office spaces for great monthly cash flow</li>
      </ul>
    </section>

    <div class="property-photo property-photo--lot" role="img" aria-label="Photo of the building row and parking lot at sunset"></div>

    <section class="headline-band">
      <h1 class="headline-band__title"><span class="headline-band__lead">For Sale</span> - Potential Income Producing<br>Commercial Office Building</h1>
      <p class="headline-band__address">42 Brenton Dr., Schaumburg, IL 60174 - Asking Price: $650,000</p>
      <div class="headline-band__divider"></div>
      <div class="brand">
        <div class="brand__name"><span class="brand__mark"></span>QTN Homes</div>
        <p class="brand__tagline">Residential &amp; Commercial</p>
      </div>
    </section>

    <section class="pitch">
      <h2 class="pitch__title">Looking to Buy or Sell?</h2>
      <p class="pitch__text">I’m your one-stop, full service licensed real estate broker. I deal with all types of real estate properties: Homes, Condos, Townhomes, Multi-Unit Apartment Buildings and Commercial Spaces.</p>
      <p class="pitch__text">Let My Experience Guide You Through Every Step of the Process!</p>
    </section>

    <div class="agent-photo" role="img" aria-label="Portrait of the managing broker"></div>

    <section class="agent">
      <p class="agent__name">Dev Marlo</p>
      <p class="agent__role">Managing Broker</p>
      <p class="agent__contact"><svg width="13" height="13" viewBox="0 0 13 13"><rect width="13" height="13" fill="#0d3fa6"/><path d="M4 3h1.8l.7 2-1 .8a5 5 0 0 0 2 2l.8-1 2 .7V9.3c0 .5-.4.8-.9.7A7 7 0 0 1 3.3 3.9c0-.5.2-.9.7-.9z" fill="#fff"/></svg>847-555-0148</p>
      <p class="agent__contact agent__contact--email"><svg width="13" height="13" viewBox="0 0 13 13"><rect width="13" height="13" fill="#0d3fa6"/><rect x="3" y="4" width="7" height="5" fill="none" stroke="#fff" stroke-width="1"/><path d="M3 4l3.5 2.8L10 4" fill="none" stroke="#fff" stroke-width="1"/></svg>dev.marlo@qtnhomes-example.com</p>
      <div class="agent__badges">
        <span class="badge badge--housing"></span>
        <span class="badge badge--listing"></span>
      </div>
    </section>

    <p class="fine-print">© 2018 QTN Homes, Inc. All Rights Reserved</p>
  </main>
</body>
</html>
```